Analytics software company needs a business card design

We need a business card design for a global analytics software provider called 'Varnel Software'. Our main focus is developing real estate analysis software. We are open to any color scheme. The final design should be simple, modern, and precise.
Updates

There is one day left in our project and we are still looking forward to receiving additional submissions. We look forward to selecting one of your designs. Thanks.

Industry/Entity Type

Real Estate

```html
<!DOCTYPE html>
<html lang="en">
<head>
<meta charset="utf-8">
<title>Varnel Software – Business Card</title>
<link rel="stylesheet" href="https://fonts.googleapis.com/css2?family=Tangerine:wght@700&family=Italianno&family=Mulish:ital,wght@1,400;1,700&display=swap">
<style>
  :root {
    --sky: #5ec4f5;
    --sky-deep: #4dbaf2;
    --sky-pale: #d9f0fc;
    --ink: #111111;
    --accent-red: #c4161c;
    --line-blue: #1f93d6;
    --teal-script: #1aa7b0;
    --paper: #ffffff;
    --lens-light: #f4f8fa;
    --lens-mid: #c9d6de;
  }
  html, body {
    margin: 0;
    padding: 0;
    width: 1200px;
    height: 1000px;
    overflow: hidden;
    background: var(--paper);
  }
  .canvas {
    position: relative;
    width: 1200px;
    height: 1000px;
  }
  .card {
    position: absolute;
    width: 640px;
    height: 360px;
    overflow: hidden;
    box-shadow: 0 6px 18px rgba(0,0,0,0.18);
  }
  .card--front {
    left: 150px;
    top: 100px;
    background: linear-gradient(150deg, var(--sky-deep) 0%, var(--sky-pale) 30%, var(--paper) 48%, var(--paper) 60%, var(--sky-pale) 85%, var(--sky) 100%);
  }
  .card--back {
    left: 410px;
    top: 540px;
    background: var(--sky);
  }
  .brand-name {
    position: absolute;
    margin: 0;
    font-family: "Tangerine", cursive;
    font-weight: 700;
    font-size: 72px;
    line-height: 1;
    color: var(--ink);
    white-space: nowrap;
  }
  .card--front .brand-name { left: 78px; top: 14px; }
  .card--back .brand-name { right: 28px; top: 42px; }
  .tagline {
    position: absolute;
    margin: 0;
    font-family: "Italianno", cursive;
    font-size: 30px;
    line-height: 1;
    white-space: nowrap;
  }
  .card--front .tagline { left: 66px; top: 86px; color: var(--accent-red); }
  .card--back .tagline { left: 20px; top: 270px; color: var(--paper); }
  .contact {
    position: absolute;
    left: 0;
    top: 140px;
    margin: 0;
    font-family: "Mulish", sans-serif;
    font-style: italic;
    font-size: 19px;
    line-height: 28px;
    color: var(--ink);
  }
  .contact span { display: block; white-space: nowrap; }
  .contact .person { margin-left: 170px; font-weight: 700; }
  .contact .role { margin-left: 164px; }
  .contact .address { margin-left: 158px; }
  .contact .phone { margin-left: 152px; }
  .contact .email { margin-left: 146px; }
  .lens-area {
    position: absolute;
    left: 430px;
    top: 62px;
    width: 170px;
    height: 170px;
    border-radius: 50%;
    background: radial-gradient(circle at 40% 35%, var(--lens-light) 0%, var(--paper) 45%, var(--lens-mid) 100%);
  }
  .specialty {
    position: absolute;
    left: 445px;
    top: 96px;
    width: 150px;
    margin: 0;
    font-family: "Italianno", cursive;
    font-size: 24px;
    line-height: 30px;
    color: var(--teal-script);
    text-align: center;
    transform: rotate(-28deg);
  }
  .ground-line {
    position: absolute;
    left: 0;
    width: 640px;
    height: 4px;
  }
  .card--front .ground-line { top: 323px; background: var(--line-blue); }
  .card--back .ground-line { top: 318px; background: var(--ink); }
</style>
</head>
<body>
<main class="canvas">

  <section class="card card--front" aria-label="Business card front">
    <h1 class="brand-name">Varnel Software</h1>
    <p class="tagline">Global Analytic Software Provider</p>
    <p class="contact">
      <span class="person">Name</span>
      <span class="role">Designation</span>
      <span class="address">Address</span>
      <span class="phone">90000000000</span>
      <span class="email">name@varnelsoft.com</span>
    </p>
    <div class="lens-area" role="img" aria-label="Magnifying glass illustration"></div>
    <p class="specialty">Specialist in<br>Real Estate<br>Analysis Software</p>
    <div class="ground-line" aria-hidden="true"></div>
  </section>

  <section class="card card--back" aria-label="Business card back">
    <h2 class="brand-name">Varnel Software</h2>
    <p class="tagline">Global Analytic Software Provider</p>
    <div class="ground-line" aria-hidden="true"></div>
  </section>

</main>
</body>
</html>
```